Small Business Consulting Firm Needs Business Card Design

Need a sleek modern business card with 2 sides matching the colors of our logo. We will be placing these with a mailer we are sending out. These business cards will only ever be given to business owners. We operate helping businesses who are struggling with cash flow or finances. If the green and blue design needs to be moved to the right of "Harborline Crest Consulting" for aesthetic purposes that is ok. We will need an editable file if possible. We would like to include the reps name, email, website, and phone number. For now just use Peter Vance, pvance@harborlinecrest.com, www.harborlinecrest.com, and 833-555-0172.

```html
<!DOCTYPE html>
<html lang="en">
<head>
<meta charset="utf-8">
<title>Harborline Crest Consulting – Business Card Front</title>
<link rel="stylesheet" href="https://fonts.googleapis.com/css2?family=Open+Sans:wght@400&display=swap">
<style>
  :root {
    --card-bg: #ffffff;
    --ink: #454545;
    --brand-green: #7ab83f;
    --brand-blue: #0a7cc4;
  }
  html, body {
    margin: 0;
    padding: 0;
    width: 1200px;
    height: 686px;
    overflow: hidden;
    background: var(--card-bg);
  }
  .card-front {
    position: relative;
    width: 1200px;
    height: 686px;
    background: var(--card-bg);
    font-family: "Open Sans", Arial, sans-serif;
    color: var(--ink);
  }
  .brand-square {
    position: absolute;
    left: 570px;
    top: 262px;
    width: 60px;
    height: 60px;
    background: var(--brand-green);
  }
  .brand-name {
    position: absolute;
    left: 0;
    right: 0;
    top: 402px;
    margin: 0;
    text-align: center;
    font-weight: 400;
    color: var(--ink);
    line-height: 1;
  }
  .brand-name__main {
    display: block;
    font-size: 56px;
    letter-spacing: 0.5px;
  }
  .brand-name__sub {
    display: block;
    margin-top: 20px;
    font-size: 26px;
    letter-spacing: 14px;
    padding-left: 14px;
  }
  .edge-tab {
    position: absolute;
    left: 1168px;
    top: 175px;
    width: 32px;
    height: 335px;
    background: var(--brand-green);
    border-radius: 32px 0 0 32px;
  }
</style>
</head>
<body>
  <main class="card-front">
    <div class="brand-square" aria-hidden="true"></div>
    <h1 class="brand-name">
      <span class="brand-name__main">HARBORLINE CREST</span>
      <span class="brand-name__sub">CONSULTING</span>
    </h1>
    <div class="edge-tab" aria-hidden="true"></div>
  </main>
</body>
</html>
```